Real Estate Flyer

I would like an A4 size flyer which has the same info 3 times and can be cut into three.
It will be used for letterbox drops for new listings (SELLING) and sold listings (SOLD). The flyer needs a heading (as above) and a space for a photo which is able to be changed for each new property. Needs to be blue, red and white. It also requires my photo, KLT logo, Marisse Thornbury logo and the following text:
"Are you considering selling? Call Marisse today for a complimentary market appraisal".
(KLT logo, Marisse Thornbury Sales Consultant logo and my photo can be found in uploaded files)
Industry/Entity Type
Real Estate
Look and feel

```html
<!DOCTYPE html>
<html lang="en">
<head>
<meta charset="utf-8">
<title>KLT Realty – Market Appraisal Flyer</title>
<link rel="stylesheet" href="https://fonts.googleapis.com/css2?family=Tinos:ital,wght@0,700;1,700&family=Questrial&display=swap">
<style>
  :root {
    --navy: #1d2f8c;
    --panel-top: #22378f;
    --panel-mid: #5a3585;
    --panel-bottom: #c8335a;
    --white: #ffffff;
    --ink: #3a3a3a;
    --muted: #8a8a8a;
    --accent: #e0279a;
    --photo-a: #c9a48e;
    --photo-b: #3a2a2e;
  }
  html, body {
    margin: 0;
    padding: 0;
    width: 1200px;
    height: 2545px;
    overflow: hidden;
    background: var(--white);
  }
  .flyer {
    position: relative;
    width: 1200px;
    height: 2545px;
    background: var(--white);
    font-family: "Tinos", "Times New Roman", serif;
  }
  .hero-panel {
    position: absolute;
    left: 0;
    top: 0;
  }
  .brand {
    position: absolute;
    left: 134px;
    top: 128px;
    display: flex;
    align-items: center;
    gap: 18px;
    font-family: "Tinos", "Times New Roman", serif;
    font-weight: 700;
    font-size: 62px;
    color: var(--white);
    line-height: 1;
  }
  .brand-mark {
    width: 46px;
    height: 46px;
    background: var(--white);
  }
  .headline {
    position: absolute;
    left: 128px;
    top: 600px;
    margin: 0;
    font-weight: 700;
    font-size: 164px;
    line-height: 170px;
    color: var(--white);
    text-shadow: 4px 5px 8px rgba(0,0,0,0.45);
  }
  .subline {
    position: absolute;
    left: 128px;
    top: 1300px;
    width: 1000px;
    margin: 0;
    font-weight: 700;
    font-style: italic;
    font-size: 102px;
    line-height: 110px;
    color: var(--white);
    text-shadow: 4px 5px 8px rgba(0,0,0,0.45);
  }
  .property-photo-slot {
    position: absolute;
    left: 640px;
    top: 1595px;
    width: 510px;
    height: 510px;
    border-radius: 50%;
    background: var(--white);
    box-shadow: 10px 14px 18px rgba(0,0,0,0.35);
  }
  .consultant {
    position: absolute;
    left: 70px;
    top: 1855px;
    display: flex;
    align-items: center;
    gap: 36px;
    font-family: "Questrial", "Arial", sans-serif;
  }
  .consultant-mark {
    width: 160px;
    height: 160px;
    border-radius: 50%;
    background: var(--accent);
  }
  .consultant-name {
    font-size: 70px;
    line-height: 80px;
    color: var(--ink);
  }
  .consultant-role {
    font-size: 40px;
    line-height: 50px;
    color: var(--muted);
  }
  .phone {
    position: absolute;
    left: 60px;
    top: 2150px;
    margin: 0;
    font-weight: 700;
    font-size: 186px;
    line-height: 1;
    letter-spacing: 2px;
    color: var(--navy);
  }
</style>
</head>
<body>
<main class="flyer">
  <svg class="hero-panel" width="1200" height="1900" viewBox="0 0 1200 1900">
    <defs>
      <linearGradient id="panelGradient" x1="0" y1="0" x2="0" y2="1">
        <stop offset="0" stop-color="var(--panel-top)"/>
        <stop offset="0.35" stop-color="var(--panel-top)"/>
        <stop offset="0.7" stop-color="var(--panel-mid)"/>
        <stop offset="1" stop-color="var(--panel-bottom)"/>
      </linearGradient>
      <radialGradient id="portraitGradient" cx="0.5" cy="0.4" r="0.6">
        <stop offset="0" stop-color="var(--photo-a)"/>
        <stop offset="1" stop-color="var(--photo-b)"/>
      </radialGradient>
      <clipPath id="panelClip">
        <path d="M62 56 H1153 V1690 Q650 1770 62 1830 Z"/>
      </clipPath>
    </defs>
    <path d="M62 56 H1153 V1690 Q650 1770 62 1830 Z" fill="url(#panelGradient)"/>
    <g clip-path="url(#panelClip)">
      <circle cx="870" cy="470" r="470" fill="url(#portraitGradient)" role="img" aria-label="Portrait photo of Marisse Thornbury, sales consultant"/>
    </g>
  </svg>

  <div class="brand">
    <span class="brand-mark"></span>
    <span class="brand-name">KLT Realty</span>
  </div>

  <h1 class="headline">Are<br>you<br>considering<br>selling?</h1>

  <p class="subline">Call Marisse today<br>for a complimentary<br>market<br>appraisal.</p>

  <div class="property-photo-slot" role="img" aria-label="Space for property photo"></div>

  <div class="consultant">
    <span class="consultant-mark"></span>
    <div class="consultant-text">
      <div class="consultant-name">Marisse<br>Thornbury</div>
      <div class="consultant-role">Sales Consultant</div>
    </div>
  </div>

  <p class="phone">0400 555 218</p>
</main>
</body>
</html>
```